Wordpress Design for Interactive Marketing Agency

We are looking to have a WP theme designed for our company, Bright Harbor Media. We are an online marketing firm specializing in SEO, Paid Search/PPC, Analytics and a number of other marketing channels.
We have a logo and tag line. We also have a rough and unloved design to work from as a way to illustrate the content needs of the homepage. We would like an interactive slider on the homepage which displays text and image content describing our services and our value props/solution positioning. Layering content is also something we'd like to incorporate in a block or two on the page, whether it be tabs, window shades, rotating or mouse-over type div swapping, scrolling news box, etc.
The design also needs to be able to transition to a less portal-like feel (re: the homepage) to a page design that houses a description for each of our services, an about page, privacy page, etc.
So, in the spirit of the typical WP construct, there would be a consistent header and footer, with a main content div that is flexible and eye-catching.
Three column design for the homepage feels right, but that's not a requirement. For the rest of the pages one or two columns seems like the right layout. Again, is this open to design.
To see what we've put together as a concept visit this page:
www.brightharbormedia.example/design/
Notes: most folks didn't care for the opaque gun in the background. Though, a subtle, muted background image would be a welcome design element. Keep in mind that these images are only for illustrating the content needs. We are not expecting anything that looks like these concepts. In fact, they didn't appeal to most of us.
Also included is a third design that we kind of liked (probably could live without the page curls, though). Modern sophistication that isn't stuffy but doesn't get too juvenile is what we're wanting. If there's a way to complement the power colors of our logo and attain a style that's lively, digerati in spirit and alluring, then that's what we would like to arrive at.
To get the latest logo:
http://brightharbormedia.example/design/Logo-Rework.png
The logo can be rearranged as needed.
I have also attached the rough designs we put together and the logo.
We really don't have any strong restrictions or absolutes as far as how the design turns out. We just want something that looks great and captures the spirit of the business/brand. The visuals could definitely benefit from a human element, or a splashy graphic or something festive, technically inclined and/or inclusive.
Updates
Project Deadline Extended
Reason: I am trying to make the project a little more accessible for designers by extending it a bit. I realize that the process can sometimes take several days, and if this allows for more submissions, there are no complaints here.
Hi Designers,
Target Market(s)
Medium-sized, regional businesses
Industry/Entity Type
Marketing
Requirements
Must have
- Theme must accomodate widgets, permalinks and all of the common WP page enhancements and taxonomy options.
Nice to have
- Most of the text on the page should be true text if possible (for SEO purposes, etc.). The ability to layer text content is also desirable, so having content blocks that use z-indexed divs would be ideal. Theme should accommodate widgets, permalinks and all of the common WP page enhancements and taxonomy options.

```html
<!DOCTYPE html>
<html lang="en">
<head>
<meta charset="utf-8">
<title>Bright Harbor Media — Online Marketing</title>
<link href="https://fonts.googleapis.com/css2?family=Ubuntu:ital,wght@0,400;0,500;0,700;1,700&display=swap" rel="stylesheet">
<style>
:root{
  --blue-deep:#0b3f9c;
  --blue-mid:#1d62cf;
  --blue-light:#4f8fe6;
  --panel-blue:#5d8fe0;
  --orange:#e8430f;
  --orange-dark:#c73205;
  --green:#2f9b2a;
  --green-dark:#1d7a1a;
  --grey-btn:#a9a9a9;
  --text:#333;
  --footer-dark:#1f1f1f;
  --field:#fffbec;
  --form-blue:#5a84b3;
  --form-bg:#d4e6fa;
  --yellow:#f7c21c;
}
*{margin:0;padding:0;box-sizing:border-box}
html,body{width:1200px;height:888px;overflow:hidden;background:#fff;font-family:'Ubuntu',sans-serif;color:var(--text)}
.canvas{position:relative;width:1200px;height:888px}
.header-band{position:absolute;left:0;top:0;width:1200px;height:359px;
  background:radial-gradient(ellipse 420px 260px at 820px 150px,#3f86ea 0%,transparent 70%),linear-gradient(180deg,#1450b8 0%,#1a5dcb 55%,#0e46a8 100%)}
.side-column{position:absolute;left:164px;top:6px;width:273px;height:530px;background:#fff}
.logo{position:absolute;left:176px;top:20px;width:250px;height:92px}
.logo-mark{position:absolute;left:160px;top:0;width:52px;height:52px;border-radius:50%;background:var(--orange)}
.logo-name{position:absolute;left:0;top:58px;font-size:19px;font-weight:700;color:var(--orange);letter-spacing:.5px;white-space:nowrap}
.logo-tag{position:absolute;right:0;top:80px;font-size:11px;font-weight:500;color:#555}
.main-nav a{position:absolute;left:188px;width:222px;height:40px;display:flex;align-items:center;justify-content:center;
  font-size:16px;font-weight:500;color:#111;text-decoration:none;letter-spacing:.3px;
  background:linear-gradient(180deg,#c4c4c4,#9d9d9d);border:1px solid #8a8a8a}
.main-nav a.active{background:linear-gradient(180deg,#f24a0f,#c73205);color:#fff;border-color:#a32a04}
.main-nav a.active::after{content:"";position:absolute;right:-14px;top:6px;border-left:14px solid #f07a0f;border-top:14px solid transparent;border-bottom:14px solid transparent}
.topbar{position:absolute;top:12px;left:490px;display:flex;align-items:center;gap:14px}
.phone{color:var(--yellow);font-size:15px}
.audit{color:#fff;font-size:15px;font-weight:500;letter-spacing:.5px}
.search-box{position:absolute;left:758px;top:11px;width:169px;height:19px;background:#fff;border:2px solid var(--yellow)}
.search-btn{position:absolute;left:938px;top:10px;width:56px;height:21px;background:var(--orange);border:1px solid #f7a070;color:#fff;font-size:10px;display:flex;align-items:center;justify-content:center}
.cycle .step{position:absolute;width:69px;height:61px;border-radius:4px;background:linear-gradient(180deg,#3fb338,var(--green-dark));border:1px solid #5ccf52;
  display:flex;align-items:center;justify-content:center;text-align:center;color:#fff;font-size:12px;font-weight:700;font-style:italic;line-height:1.3}
.cycle .hub{position:absolute;left:585px;top:156px;width:90px;height:89px;border-radius:4px;background:linear-gradient(180deg,#2f9b2a,#166e14);border:1px solid #5ccf52;
  display:flex;align-items:center;justify-content:center;text-align:center;color:#fff;font-size:16px;font-weight:700;font-style:italic;line-height:1.6}
.cycle-arrows{position:absolute;left:0;top:0}
.regions{position:absolute;left:817px;top:64px;width:201px;height:285px;background:var(--panel-blue);border:1px solid #8db3f0;border-radius:3px}
.regions h2{font-size:20px;font-weight:400;color:#0c2b66;text-align:center;line-height:21px;margin-top:9px}
.regions .rule{height:3px;background:#8ab0ee;margin:4px 6px 0}
.badges{display:flex;gap:8px;justify-content:center;margin-top:13px}
.badge{width:75px;height:74px;background:#fff;border:1px solid #c8d8f2;border-radius:3px}
.regions p{font-size:11px;line-height:15.5px;color:#0c2b66;text-align:center;margin:9px 8px 0}
.contact{position:absolute;left:168px;top:382px;width:264px;height:246px;background:var(--form-bg);border:1px solid #b4cdea}
.contact-inner{position:absolute;left:11px;top:11px;width:242px;height:187px;background:var(--form-blue);border:1px solid #7c9dc4}
.field{position:absolute;left:10px;width:219px;background:var(--field);font-size:12px;color:#555;padding:4px 7px}
.send{position:absolute;left:103px;top:210px;width:54px;height:25px;background:linear-gradient(180deg,#4b78a8,#2a5485);color:#fff;font-size:12px;display:flex;align-items:center;justify-content:center;border:1px solid #1e4470}
.welcome{position:absolute;left:465px;top:388px;width:540px}
.welcome h1{font-size:16px;font-weight:400;color:#111;margin-bottom:17px}
.welcome p{font-size:10.6px;line-height:15.4px;color:#333;margin-bottom:15.4px;padding-left:3px}
.welcome a{font-size:11px;color:var(--orange-dark);padding-left:3px}
.welcome a span{color:#999;text-decoration:none}
.services-band{position:absolute;left:168px;top:654px;width:852px;height:152px;background:var(--footer-dark)}
.services-band .divider{position:absolute;top:8px;width:1px;height:136px;background:#3c3c3c}
.services-band ul{position:absolute;top:18px;list-style:none}
.services-band li{font-size:10px;color:#f0f0f0;height:20.6px;letter-spacing:.2px}
.art{position:absolute;top:19px;border:2px solid #ddd;border-radius:3px}
.footer-links{position:absolute;left:174px;top:834px;font-size:10px;color:#666;display:flex;gap:11px}
.social{position:absolute;left:824px;top:826px;display:flex;gap:6px}
.social span{width:19px;height:19px;border-radius:2px}
.accredited{position:absolute;left:934px;top:818px;width:82px;height:35px;background:#1a6a8c;border-radius:3px}
.copyright{position:absolute;right:189px;top:860px;font-size:10px;color:#666}
</style>
</head>
<body>
<div class="canvas">
  <div class="header-band"></div>
  <div class="side-column"></div>

  <div class="logo">
    <span class="logo-mark"></span>
    <span class="logo-name">BRIGHT HARBOR MEDIA</span>
    <span class="logo-tag">Online Marketing. Bright Harbor.</span>
  </div>

  <nav class="main-nav">
    <a href="#" style="top:126px">PAID SEARCH</a>
    <a href="#" class="active" style="top:175px">SEO</a>
    <a href="#" style="top:223px">DISPLAY ADS</a>
    <a href="#" style="top:272px">ANALYTICS</a>
    <a href="#" style="top:320px">PERFORMANCE</a>
  </nav>

  <div class="topbar"><span class="phone">1 800 555 0142</span><span class="audit">GET A FREE AUDIT!</span></div>
  <div class="search-box"></div>
  <div class="search-btn">SEARCH</div>

  <div class="cycle">
    <svg class="cycle-arrows" width="1200" height="360" fill="none" stroke="#e6eefb" stroke-width="6">
      <path d="M546 108 V90 H566"/><path d="M562 82 L576 90 L562 98" fill="#e6eefb" stroke="none"/>
      <path d="M704 83 H724 V104"/><path d="M716 100 L724 114 L732 100" fill="#e6eefb" stroke="none"/>
      <path d="M729 193 V208"/><path d="M721 205 L729 219 L737 205" fill="#e6eefb" stroke="none"/>
      <path d="M728 302 V318 H712"/><path d="M716 310 L702 318 L716 326" fill="#e6eefb" stroke="none"/>
      <path d="M549 300 V324 H562"/><path d="M541 304 L549 292 L557 304" fill="#e6eefb" stroke="none"/>
      <path d="M531 214 V198"/><path d="M523 202 L531 188 L539 202" fill="#e6eefb" stroke="none"/>
    </svg>
    <div class="step" style="left:594px;top:63px">Building<br>Strategy</div>
    <div class="step" style="left:694px;top:123px">SEO<br>Keyword<br>Research</div>
    <div class="step" style="left:696px;top:225px">Optimizing<br>Your<br>Site</div>
    <div class="step" style="left:595px;top:284px">Link<br>Building<br>Strategy</div>
    <div class="step" style="left:496px;top:219px">Directory<br>Listings</div>
    <div class="step" style="left:496px;top:123px">Weekly<br>Monitoring</div>
    <div class="hub">SEO<br>SERVICES</div>
  </div>

  <aside class="regions">
    <h2>Online Marketing<br>Dallas Austin<br>Houston</h2>
    <div class="rule"></div>
    <div class="badges"><div class="badge"></div><div class="badge"></div></div>
    <div class="rule"></div>
    <p>Bright Harbor Media is a full-service Internet marketing agency providing Paid Search (PPC) Search Engine Optimization (SEO), Display Advertising, Analytics Consulting, Creative Direction, and....</p>
  </aside>

  <form class="contact">
    <div class="contact-inner">
      <div class="field" style="top:10px;height:25px">Name:</div>
      <div class="field" style="top:57px;height:25px">Email:</div>
      <div class="field" style="top:103px;height:99px;top:103px;height:86px">How can we help you?</div>
    </div>
    <div class="send">SEND</div>
  </form>

  <section class="welcome">
    <h1>WELCOME &gt;&gt;</h1>
    <p>Lorem Ipsum is simply dummy text of the printing and typesetting industry. Lorem Ipsum has been the industry's standard dummy text ever since the 1500s, when an unknown printer took a galley of type and scrambled it to make a type specimen book. It has survived not only five centuries, but also the leap into electronic typesetting, remaining essentially unchanged. It was popularised in the 1960s with the release of Typesheet sheets containing Lorem Ipsum passages, and more recently with desktop publishing software like Quillset PageComposer including versions of Lorem Ipsum.</p>
    <p>Lorem Ipsum is simply dummy text of the printing and typesetting industry. Lorem Ipsum has been the industry's standard dummy text ever since the 1500s, when an unknown printer took a galley of type and scrambled it to make a type specimen book.</p>
    <a href="#">Read More</a> <a href="#"><span>»</span></a>
  </section>

  <section class="services-band">
    <ul style="left:12px"><li>LOCAL SEO</li><li>LINK BUILDING</li><li>CONTENT</li><li>DESIGN</li><li>DEVELOPMENT</li><li>MOBILE</li></ul>
    <div class="art" role="img" aria-label="Two smartphones showing a map app" style="left:98px;width:105px;height:113px;background:linear-gradient(135deg,#e8e8e8,#8d8d8d)"></div>
    <div class="divider" style="left:246px"></div>
    <ul style="left:282px"><li>ATTRIBUTION TRACKING</li><li>CALL TRACKING</li><li>PAY FOR PERFORMANCE</li><li>AFFILIATE MARKETING</li><li>RETARGETING</li><li>LANDING PAGE TESTING</li></ul>
    <div class="art" role="img" aria-label="Diagram of devices routing calls to a tracking hub" style="left:422px;width:109px;height:113px;background:linear-gradient(180deg,#f4f6fa,#c9d6ea)"></div>
    <div class="divider" style="left:571px"></div>
    <ul style="left:601px"><li>SOCIAL MEDIA</li><li>VIDEO COMMERCE</li><li>CUSTOM ANALYTICS</li><li>CUSTOM REPORTING</li><li>RETARGETING</li></ul>
    <div class="art" role="img" aria-label="Social media word cloud" style="left:715px;width:127px;height:113px;background:radial-gradient(circle,#f6efe6,#b58f6a)"></div>
  </section>

  <nav class="footer-links"><span>Privacy Policy</span><span>|</span><span>Terms of Service</span><span>|</span><span>About Us</span><span>|</span><span>Contact Us</span><span>|</span><span>Our Blog</span></nav>
  <div class="social"><span style="background:#3b5b9a"></span><span style="background:#4ab2e6"></span><span style="background:#1a6a8c"></span></div>
  <div class="accredited"></div>
  <div class="copyright">© Copyright 2012 Bright Harbor Media, LLC</div>
</div>
</body>
</html>
```